Upmarket Bathroom and Kitchen ware supplier needs a classy business card design

We are a company based in Fiji, we sell plumbing ware (Kitchen and bathroom taps, Basins,showers, toilets etc) through up market show rooms to individuals and directly through Architects and designers of resorts and holiday houses for new builds and renovations. we are wanting to upgrade our over all look and brand. we are starting with a new logo but will be rebranding the whole business. This project is for a business card design for my management and tales team I would like it to be dark, classy and interesting

Target Market(s)

Resort directors and Management, High end holiday home owners

Contact Information for Business Card

Neil Dawson
Director
+64219473815

Colors

Designer to choose colors to be used in the design.

Requirements
Must have
• Must have an upmarket appearance I like darker charcoal shades but will be guided by the designers
• Please any catch phrases like "Crafting remarkable living rooms" this belongs tpo one of our suppliers so can not be used.
Nice to have
• Double sided, so front dedicated to logo provided and back info about the business and the person.

```html
<!DOCTYPE html>
<html lang="en">
<head>
<meta charset="UTF-8">
<title>Coralline Interiors – Business Card</title>
<link rel="stylesheet" href="https://fonts.googleapis.com/css2?family=Open+Sans:wght@300;400;700&display=swap">
<style>
  :root {
    --backdrop: #202226;
    --card-white: #fbfbfc;
    --card-navy: #15173a;
    --ink: #1b1c2e;
    --ink-soft: #55575f;
    --band: #0b0d0c;
    --on-dark: #ffffff;
  }
  * { box-sizing: border-box; margin: 0; padding: 0; }
  html, body {
    width: 1200px; height: 900px; overflow: hidden;
    background: var(--backdrop);
    font-family: "Open Sans", Arial, sans-serif;
  }
  .canvas {
    width: 1200px; height: 900px;
    display: flex; flex-direction: column;
    align-items: center; justify-content: center; gap: 60px;
  }
  .card {
    position: relative;
    width: 630px; height: 360px;
    box-shadow: 0 18px 40px rgba(0,0,0,.45);
  }
  /* Personal side */
  .card--info { background: var(--card-white); color: var(--ink); }
  .card__tab {
    position: absolute; left: 0; top: 34px;
    width: 7px; height: 20px; background: var(--card-navy);
  }
  .card__person { position: absolute; left: 38px; top: 30px; }
  .card__name { font-weight: 700; font-size: 27px; line-height: 1.1; }
  .card__role { font-size: 14px; color: var(--ink-soft); margin-top: 4px; }
  .card__contacts {
    position: absolute; left: 38px; top: 118px;
    list-style: none; font-size: 13.5px; color: var(--ink);
  }
  .card__contacts li { display: flex; align-items: center; gap: 14px; margin-bottom: 7px; }
  .card__contacts svg { width: 13px; height: 13px; stroke: var(--ink-soft); fill: none; stroke-width: 1.6; }
  .card__band {
    position: absolute; left: 0; right: 0; bottom: 0; height: 56px;
    background: var(--band); color: var(--on-dark);
    display: flex; align-items: center; padding-left: 100px;
    font-size: 22px; letter-spacing: .5px;
  }
  .wordmark {
    display: flex; align-items: center; gap: 12px;
    font-weight: 300; text-transform: uppercase; letter-spacing: 8px;
    white-space: nowrap;
  }
  .wordmark__dot { width: 12px; height: 12px; border-radius: 50%; background: currentColor; }
  .wordmark__name { font-size: 25px; line-height: 1.3; }
  .card--info .wordmark { position: absolute; right: 38px; bottom: 84px; color: var(--ink); }
  /* Brand side */
  .card--brand { background: var(--card-navy); color: var(--on-dark); display: flex; align-items: center; justify-content: center; }
</style>
</head>
<body>
<main class="canvas">
  <section class="card card--info" aria-label="Business card, personal side">
    <span class="card__tab"></span>
    <div class="card__person">
      <h1 class="card__name">Neil Dawson</h1>
      <p class="card__role">Director</p>
    </div>
    <ul class="card__contacts">
      <li><svg viewBox="0 0 16 16"><path d="M4 1.5l2.2 3-1.4 1.6c.9 2 2.5 3.6 4.6 4.6l1.6-1.4 3 2.2-1.3 2.5C7 14 2 9 1.5 2.8z"/></svg>+642 194 73815</li>
      <li><svg viewBox="0 0 16 16"><rect x="1.5" y="3.5" width="13" height="9" rx="1"/><path d="M1.5 4l6.5 5 6.5-5"/></svg>hello@coralline.fj</li>
      <li><svg viewBox="0 0 16 16"><circle cx="8" cy="8" r="2.6"/><path d="M10.6 5.5v3.7c0 1.6 2.9 1.6 2.9-1.2A5.5 5.5 0 1 0 11 12.6"/></svg>www.coralline.fj</li>
    </ul>
    <div class="wordmark">
      <span class="wordmark__dot"></span>
      <span class="wordmark__name">Coralline Interiors</span>
    </div>
    <div class="card__band">www.coralline.fj</div>
  </section>

  <section class="card card--brand" aria-label="Business card, brand side">
    <div class="wordmark">
      <span class="wordmark__dot"></span>
      <span class="wordmark__name">Coralline Interiors</span>
    </div>
  </section>
</main>
</body>
</html>
```